Hot Offer banner for product listing page

Hi, we need a banner in the dimensions 210x390px which will be shown in the product listing on our online shop. There are 18 products and in between randomly there should be 3 banners with three different information.
first banner: fast delivery
The idea is to show a stove which is very "fast". Maybe you can make an effect like in Voidcruiser Halcyon when they activate the warp drive or something similar. Anyway, the banner should indicate that the delivery is very fast for this product.

second banner: Advantage banner
We would like to have a banner which names all our advantages in our online shop. this is the list of advantages:
- over 200,000 satisfied customers
- Best price guarantee
- thousands of devices in stock
- Top ratings

I attached you some examples, just to give you an idea.

```html
<!DOCTYPE html>
<html lang="en">
<head>
<meta charset="utf-8">
<title>Shop Banners</title>
<link href="https://fonts.googleapis.com/css2?family=Source+Sans+3:wght@600&display=swap" rel="stylesheet">
<style>
  :root {
    --stage: #bcbdbf;
    --orange: #f0803c;
    --paper: #f3f3f4;
    --ink: #4a4a4c;
    --rule: #8a8a8c;
  }
  html, body { margin: 0; padding: 0; overflow: hidden; }
  body {
    width: 1199px; height: 1200px;
    background: var(--stage);
    position: relative;
    font-family: "Source Sans 3", "Source Sans Pro", sans-serif;
    font-weight: 600;
    color: var(--ink);
  }
  .banner {
    position: absolute;
    top: 266px;
    width: 359px; height: 668px;
    overflow: hidden;
  }
  .banner--delivery { left: 200px; background: var(--orange); }
  .banner--advantages { left: 639px; background: var(--paper); }

  .delivery-visual {
    position: absolute;
    left: 128px; top: 40px;
    width: 104px; height: 400px;
    background: linear-gradient(180deg, rgba(255,255,255,0.18) 0%, rgba(255,255,255,0.1) 55%, rgba(250,200,110,0.7) 68%, rgba(246,170,100,0.6) 100%);
    border-radius: 12px 12px 40px 40px;
  }
  .clouds { position: absolute; left: 0; top: 0; }
  .delivery-title {
    position: absolute;
    left: 0; right: 0; top: 456px;
    margin: 0;
    text-align: center;
    font-size: 45px;
    line-height: 48px;
    letter-spacing: 0.3px;
  }

  .advantage {
    position: absolute;
    left: 0; right: 0;
    text-align: center;
  }
  .advantage svg { display: block; margin: 0 auto; }
  .advantage p {
    margin: 0;
    font-size: 23px;
    line-height: 28px;
  }
  .divider {
    position: absolute;
    left: 66px; width: 227px;
    border-top: 1.5px dashed var(--rule);
  }
  .icon { fill: none; stroke: var(--orange); stroke-width: 2; stroke-linejoin: round; stroke-linecap: round; }
</style>
</head>
<body>

<section class="banner banner--delivery">
  <div class="delivery-visual" role="img" aria-label="Stove lifting off like a rocket with a flame trail"></div>
  <svg class="clouds" width="359" height="668" viewBox="0 0 359 668" aria-hidden="true">
    <g fill="var(--paper)">
      <circle cx="100" cy="431" r="59"/>
      <circle cx="40" cy="460" r="45"/>
      <circle cx="175" cy="500" r="66"/>
      <circle cx="257" cy="470" r="41"/>
      <circle cx="333" cy="489" r="33"/>
      <rect x="0" y="418" width="359" height="250"/>
    </g>
  </svg>
  <h2 class="delivery-title">Fast<br>Delivery</h2>
</section>

<section class="banner banner--advantages">
  <div class="advantage" style="top:44px">
    <svg class="icon" width="64" height="56" viewBox="0 0 64 56">
      <path d="M32 3l2 4 4.5.5-3.3 3 .9 4.4L32 12.7l-4.1 2.2.9-4.4-3.3-3L30 7z"/>
      <path d="M11 11l1.5 3 3.3.4-2.4 2.2.6 3.2L11 18.3l-3 1.5.6-3.2-2.4-2.2 3.3-.4z"/>
      <path d="M53 11l1.5 3 3.3.4-2.4 2.2.6 3.2L53 18.3l-3 1.5.6-3.2-2.4-2.2 3.3-.4z"/>
      <circle cx="32" cy="29" r="6"/>
      <circle cx="16" cy="35" r="5"/>
      <circle cx="48" cy="35" r="5"/>
      <path d="M20 54v-5a12 12 0 0 1 24 0v5z"/>
      <path d="M4 54v-3a10 10 0 0 1 14-9"/>
      <path d="M60 54v-3a10 10 0 0 0-14-9"/>
      <path d="M4 54h56"/>
    </svg>
    <p style="margin-top:6px">Over 200,000<br>satisfied customers</p>
  </div>
  <div class="divider" style="top:183px"></div>

  <div class="advantage" style="top:204px">
    <svg class="icon" width="70" height="58" viewBox="0 0 70 58">
      <rect x="3" y="30" width="8" height="24"/>
      <path d="M11 32l10-8 4-14c4 0 6 3 5 8l-2 8h10a3 3 0 0 1 0 6h-2a3 3 0 0 1 0 6h-2a3 3 0 0 1 0 6h-3a3 3 0 0 1 0 6H18l-7-3"/>
      <path d="M46 10l8-8 8 8v44H46z"/>
      <circle cx="54" cy="11" r="2"/>
      <path d="M57 24h-4a2.5 2.5 0 0 0 0 5h2a2.5 2.5 0 0 1 0 5h-4M54 21v16"/>
    </svg>
    <p style="margin-top:4px">Best price<br>guarantee</p>
  </div>
  <div class="divider" style="top:345px"></div>

  <div class="advantage" style="top:365px">
    <svg class="icon" width="66" height="64" viewBox="0 0 66 64">
      <path d="M22 8l12-6 12 6v12l-12 6-12-6z M22 8l12 6 12-6 M34 14v12"/>
      <path d="M4 36l12-6 12 6v12l-12 6-12-6z M4 36l12 6 12-6 M16 42v12"/>
      <path d="M34 36l12-6 12 6v12l-12 6-12-6z M34 36l12 6 12-6 M46 42v12"/>
      <circle cx="50" cy="25" r="8" fill="var(--paper)"/>
      <path d="M46 25l3 3 5-6"/>
    </svg>
    <p style="margin-top:8px">Thousands of<br>devices in stock</p>
  </div>
  <div class="divider" style="top:508px"></div>

  <div class="advantage" style="top:527px">
    <svg class="icon" width="70" height="66" viewBox="0 0 70 66">
      <g id="star">
        <path d="M35 2l3 6 6.5.8-4.8 4.5 1.3 6.5L35 16.6l-6 3.2 1.3-6.5-4.8-4.5 6.5-.8z"/>
      </g>
      <path d="M12 22l3 6 6.5.8-4.8 4.5 1.3 6.5L12 36.6l-6 3.2 1.3-6.5-4.8-4.5 6.5-.8z"/>
      <path d="M58 22l3 6 6.5.8-4.8 4.5 1.3 6.5L58 36.6l-6 3.2 1.3-6.5-4.8-4.5 6.5-.8z"/>
      <path d="M20 44l3 6 6.5.8-4.8 4.5 1.3 6.5L20 58.6l-6 3.2 1.3-6.5-4.8-4.5 6.5-.8z"/>
      <path d="M50 44l3 6 6.5.8-4.8 4.5 1.3 6.5L50 58.6l-6 3.2 1.3-6.5-4.8-4.5 6.5-.8z"/>
    </svg>
    <p style="margin-top:2px">Top ratings</p>
  </div>
</section>

</body>
</html>
```